Lotus Ridge Property Development Co.

We need a logo and business card design for a Hong Kong based real estate company, KVO Estates. We are want the brand to reflect the owners forward thinking, creative, and trend setting projects, while also reflecting a sense of security and strength. We invest in industrial properties which we convert to co-living or co-working spaces. KVO stands for Greater Bay Area which is the region around southern China including HK, Macau, and 9 other Chinese cities...made up of approx. 68 million people. There are massive infrastructure projects including the bridge to Macau and high-speed rail to SZ and the bridge connecting SZ and Zhongshan.

Target Market(s)

Chinese and western retail investors, as well as institutional investors

Industry/Entity Type

Real Estate Development

Contact Information for Business Card

Tom Whitlow
CEO
tom@kvoestates-mail.com
M + 852 9418 2650
F + 852 3264 5172
Suite 2207, The Arbor, 41 Kestrel Rd., Central, Hong Kong

Logo Text

kvo estates (company name) lifestyle property development (underneath)

Colors

Designer to choose colors to be used in the design.

Requirements
Must have
• Details listed above. One side should include the logo and company name...kvo estates in modern, hip styling with "lifestyle property development"
Nice to have
• Could be a Black card, with metallic purple "kvo" and white "land"...but open great design ideas
Should not have
• boring and traditional layout

```html
<!DOCTYPE html>
<html lang="en">
<head>
<meta charset="utf-8">
<title>KVO Estates – Business Card</title>
<link rel="stylesheet" href="https://fonts.googleapis.com/css2?family=Open+Sans:wght@400;600;700&family=Arimo:wght@400;700&display=swap">
<style>
  :root {
    --page-bg: #353535;
    --card-top: #2c2c2c;
    --card-bottom: #1e1e1e;
    --ink: #d6d6d6;
    --ink-soft: #c4c4c4;
  }
  * { margin: 0; padding: 0; box-sizing: border-box; }
  html, body {
    width: 1042px; height: 1200px; overflow: hidden;
    background: var(--page-bg);
    font-family: "Open Sans", sans-serif;
    color: var(--ink);
  }
  .canvas { position: relative; width: 1042px; height: 1200px; }
  .card {
    position: absolute; left: 170px; width: 714px; height: 420px;
    border-radius: 22px;
    background: radial-gradient(ellipse at 50% 40%, var(--card-top) 0%, var(--card-bottom) 80%);
  }
  .card--front { top: 126px; }
  .card--back { top: 616px; }

  .brand {
    position: absolute; text-align: center;
    font-family: "Open Sans", sans-serif; font-weight: 700; color: var(--ink);
  }
  .brand__name { display: flex; align-items: center; gap: 12px; white-space: nowrap; }
  .brand__mark { width: 22px; height: 22px; background: var(--ink); flex: none; }
  .brand__tagline { font-weight: 600; letter-spacing: 0.5px; color: var(--ink); }

  .card--front .brand { left: 0; right: 0; top: 130px; display: flex; flex-direction: column; align-items: center; }
  .card--front .brand__name { font-size: 44px; line-height: 1.1; }
  .card--front .brand__tagline { font-size: 13px; margin-top: 8px; }

  .address {
    position: absolute; left: 0; right: 0; top: 355px;
    text-align: center; font-size: 17.5px; color: var(--ink-soft);
  }

  .card--back .brand { left: 120px; top: 165px; display: flex; flex-direction: column; align-items: flex-start; }
  .card--back .brand__name { font-size: 30px; line-height: 1.1; gap: 9px; }
  .card--back .brand__mark { width: 16px; height: 16px; }
  .card--back .brand__tagline { font-size: 10px; margin-top: 6px; }

  .divider { position: absolute; left: 340px; top: 133px; width: 2px; height: 160px; background: var(--ink-soft); }

  .person { position: absolute; left: 366px; top: 128px; font-family: "Arimo", sans-serif; }
  .person__name { font-size: 26px; color: var(--ink); letter-spacing: 0.3px; }
  .person__name b { font-weight: 700; }
  .person__role { display: flex; align-items: center; gap: 8px; margin-top: 2px; font-size: 19px; font-weight: 700; letter-spacing: 1.5px; padding-left: 2px; }
  .person__role::after { content: ""; width: 134px; height: 2px; background: var(--ink-soft); }

  .contacts { position: absolute; left: 372px; top: 214px; list-style: none; }
  .contacts li { display: flex; align-items: center; gap: 8px; height: 28px; font-size: 19px; color: var(--ink-soft); }
  .contacts svg { width: 13px; height: 13px; fill: var(--ink-soft); flex: none; }
</style>
</head>
<body>
<main class="canvas">
  <section class="card card--front">
    <div class="brand">
      <div class="brand__name"><span class="brand__mark"></span>KVO Estates</div>
      <div class="brand__tagline">lifestyle property development</div>
    </div>
    <p class="address">Suite 2207, The Arbor, 41 Kestrel Rd, Central, Hong Kong</p>
  </section>

  <section class="card card--back">
    <div class="brand">
      <div class="brand__name"><span class="brand__mark"></span>KVO Estates</div>
      <div class="brand__tagline">lifestyle property development</div>
    </div>
    <div class="divider"></div>
    <div class="person">
      <div class="person__name"><b>TOM</b> WHITLOW</div>
      <div class="person__role">CEO</div>
    </div>
    <ul class="contacts">
      <li>
        <svg viewBox="0 0 24 24" aria-hidden="true"><path d="M6.6 10.8a15.1 15.1 0 0 0 6.6 6.6l2.2-2.2a1 1 0 0 1 1-.25 11.4 11.4 0 0 0 3.6.57 1 1 0 0 1 1 1V20a1 1 0 0 1-1 1A17 17 0 0 1 3 4a1 1 0 0 1 1-1h3.5a1 1 0 0 1 1 1c0 1.25.2 2.45.57 3.57a1 1 0 0 1-.25 1z"/></svg>
        852 9418 2650
      </li>
      <li>
        <svg viewBox="0 0 24 24" aria-hidden="true"><path d="M6 2h12v5H6zM3 8h18a1 1 0 0 1 1 1v8h-4v5H6v-5H2V9a1 1 0 0 1 1-1zm5 8v4h8v-4z"/></svg>
        852 3264 5172
      </li>
      <li>
        <svg viewBox="0 0 24 24" aria-hidden="true"><path d="M2 5h20v14H2zm2 2v.5l8 5.5 8-5.5V7l-8 5.5z"/></svg>
        tom@kvoestates-mail.com
      </li>
    </ul>
  </section>
</main>
</body>
</html>
```